Etiketten-Design für Weinflaschen gesucht
Zielgruppe
Wir sind ein Weingut und suchen für unsere Weinflaschen ein neues Etikettdesign.
Aufgabenstellung
Im Anhang sieht man unsere leeren Weinflaschen mit den neuen Kapseln. Dazu passend suchen wir die Etiketten.
Grundfarbe des Etikettes ist Weiß, Größe ca. 11cm hoch & 9cm breit!
Jede Sorte hat ihrer eigene Farbe - diese ist am Kapsel sichtbar und soll sich auch leicht im Etikett
wieder finden.
Etiketten vom Grunddesign gleich + jedoch nur an STELLEN ANDERS EINGEFÄRBT.
Am Etikett zu finden sollte sein:
- Unser Logo mit Namen (Weingut muss nicht vorhanden sein am Etikett)
- Kirchenlogo
- Sorte von Wein:
(Grüner Veltliner - Grün
Traminer - Blau
Rheinriesling - Orange
Blaufränkisch - Rot
St.Lauerent -Gelb
Zweigelt - Weiß)

```html
<!DOCTYPE html>
<html lang="de">
<head>
<meta charset="utf-8">
<title>Rebenhain – Etikett Traminer</title>
<link rel="stylesheet" href="https://fonts.googleapis.com/css2?family=Raleway:wght@300&display=swap">
<style>
  :root {
    --backdrop: #c99d68;
    --label-white: #ffffff;
    --ink: #0d0d0d;
    --variety-blue: #3457a4;
    --gold-deep: #d2a14e;
    --gold-pale: #f4f0b6;
    --gold-mid: #ddc27c;
    --measure-red: #e3251b;
  }
  html, body {
    margin: 0;
    padding: 0;
    width: 1200px;
    height: 848px;
    overflow: hidden;
    background: var(--backdrop);
    font-family: "Raleway", sans-serif;
  }
  .canvas {
    position: relative;
    width: 1200px;
    height: 848px;
  }
  .measure-lines {
    position: absolute;
    inset: 0;
  }
  .measure-label {
    position: absolute;
    color: var(--measure-red);
    font-weight: 300;
    font-size: 31px;
    line-height: 1;
    white-space: nowrap;
  }
  .measure-width { left: 543px; top: 24px; }
  .measure-height { left: 911px; top: 420px; }

  .wine-label {
    position: absolute;
    left: 312px;
    top: 97px;
    width: 550px;
    height: 672px;
    background: var(--label-white);
    overflow: hidden;
  }
  .label-graphics {
    position: absolute;
    inset: 0;
    width: 100%;
    height: 100%;
  }
  .brand-name {
    position: absolute;
    left: 0;
    top: 178px;
    width: 574px;
    text-align: center;
    color: var(--ink);
    font-weight: 300;
    font-size: 54px;
    letter-spacing: 1px;
    line-height: 1;
  }
  .variety-name {
    position: absolute;
    left: 71px;
    top: 356px;
    color: var(--ink);
    font-weight: 300;
    font-size: 25px;
    letter-spacing: 0.5px;
    line-height: 1;
  }
  .church-artwork {
    position: absolute;
    left: 353px;
    top: 495px;
    width: 178px;
    height: 161px;
    background: linear-gradient(160deg, #d9d9d9 0%, #6a6a6a 55%, #2e2e2e 100%);
    border-radius: 4px;
  }
</style>
</head>
<body>
<div class="canvas">
  <svg class="measure-lines" width="1200" height="848" viewBox="0 0 1200 848" aria-hidden="true">
    <defs>
      <marker id="arrow-head" viewBox="0 0 10 10" refX="9" refY="5" markerWidth="7" markerHeight="7" orient="auto-start-reverse">
        <path d="M0 0 L10 5 L0 10 Z" fill="#e3251b"/>
      </marker>
    </defs>
    <line x1="314" y1="69" x2="860" y2="69" stroke="#e3251b" stroke-width="1.6" marker-start="url(#arrow-head)" marker-end="url(#arrow-head)"/>
    <line x1="897" y1="98" x2="897" y2="768" stroke="#e3251b" stroke-width="1.6" marker-start="url(#arrow-head)" marker-end="url(#arrow-head)"/>
  </svg>
  <div class="measure-label measure-width">9 cm</div>
  <div class="measure-label measure-height">11 cm</div>

  <section class="wine-label">
    <svg class="label-graphics" viewBox="0 0 537 655" preserveAspectRatio="none" aria-hidden="true">
      <defs>
        <linearGradient id="gold-edge" x1="0" y1="1" x2="1" y2="0">
          <stop offset="0" stop-color="#d2a14e"/>
          <stop offset="0.55" stop-color="#f4f0b6"/>
          <stop offset="1" stop-color="#ddc27c"/>
        </linearGradient>
      </defs>
      <polygon class="variety-band-edge" points="129,655 537,123 537,247 226,655" fill="url(#gold-edge)"/>
      <polygon class="variety-band" points="139,655 537,137 537,235 217,655" fill="#3457a4"/>
      <circle class="band-dot" cx="397" cy="372" r="24" fill="#ffffff"/>
      <circle class="brand-dot" cx="289" cy="103" r="45" fill="#0d0d0d"/>
    </svg>
    <div class="brand-name">Rebenhain</div>
    <div class="variety-name">TRAMINER</div>
    <div class="church-artwork" role="img" aria-label="Federzeichnung der Dorfkirche auf einem Hügel"></div>
  </section>
</div>
</body>
</html>
```